Construction business card

I need a new business card, they can connect with my logo, brand.
What we do is residential house , design and build
I like: Navy blue / black
I attached our logo, brand,
and, some idea for business card.

```html
<!DOCTYPE html>
<html lang="en">
<head>
<meta charset="utf-8">
<title>Harlow Building Group – Business Card</title>
<link href="https://fonts.googleapis.com/css2?family=Montserrat:wght@400;500;700&display=swap" rel="stylesheet">
<style>
  :root {
    --backdrop: #1d1d1f;
    --card: #0d0d0e;
    --card-edge: #161618;
    --gloss: #2c2c30;
    --accent: #5b86d6;
    --text: #f2f2f2;
    --muted: #cfd3da;
  }
  * { margin: 0; padding: 0; box-sizing: border-box; }
  html, body {
    width: 1200px; height: 900px; overflow: hidden;
    background: var(--backdrop);
    font-family: "Montserrat", sans-serif;
  }
  .canvas { position: relative; width: 1200px; height: 900px; }

  .card {
    position: absolute;
    width: 600px; height: 343px;
    background: var(--card);
    border: 1px solid var(--card-edge);
    box-shadow: 0 18px 40px rgba(0,0,0,.55);
  }
  .card--front { left: 90px; top: 90px; }
  .card--back { left: 510px; top: 470px; }

  /* front: tonal gloss wordmark */
  .front-mark {
    position: absolute; inset: 0;
    display: flex; align-items: center; justify-content: center; gap: 14px;
  }
  .front-mark__square { width: 22px; height: 22px; background: var(--gloss); }
  .front-mark__name {
    color: var(--gloss);
    font-weight: 700; font-size: 30px; letter-spacing: 2px;
    text-transform: uppercase;
  }

  /* back */
  .brand {
    position: absolute; right: 36px; top: 58px;
    display: flex; align-items: center; gap: 10px;
  }
  .brand__square { width: 16px; height: 16px; background: var(--accent); }
  .brand__name {
    color: var(--text); font-weight: 700; font-size: 20px;
    letter-spacing: 1px; text-transform: uppercase;
  }

  .edge-tab {
    position: absolute; left: 0; top: 140px;
    width: 12px; height: 26px; background: var(--accent);
  }
  .person { position: absolute; left: 44px; top: 126px; }
  .person__name {
    color: var(--accent); font-weight: 700; font-size: 19px;
    text-transform: uppercase; letter-spacing: .5px;
  }
  .person__role { color: var(--text); font-size: 14px; margin-top: 2px; }

  .address {
    position: absolute; left: 96px; top: 205px;
    color: var(--muted); font-size: 13px; line-height: 1.4; font-style: normal;
  }
  .contacts {
    position: absolute; left: 96px; top: 255px;
    list-style: none; color: var(--muted); font-size: 13px;
  }
  .contacts li { display: flex; align-items: center; gap: 8px; line-height: 1.55; }
  .contacts svg { width: 12px; height: 12px; fill: var(--accent); flex: none; }
</style>
</head>
<body>
<main class="canvas">

  <section class="card card--front" aria-label="Card front">
    <div class="front-mark">
      <span class="front-mark__square"></span>
      <span class="front-mark__name">Harlow Building Group</span>
    </div>
  </section>

  <section class="card card--back" aria-label="Card back">
    <div class="brand">
      <span class="brand__square"></span>
      <span class="brand__name">Harlow Building Group</span>
    </div>

    <span class="edge-tab"></span>
    <div class="person">
      <p class="person__name">Dalton Reyes</p>
      <p class="person__role">Founder &amp; CEO</p>
    </div>

    <address class="address">48 Ashgrove St,<br>Kelvin Park, VIC 3190</address>

    <ul class="contacts">
      <li>
        <svg viewBox="0 0 24 24" aria-hidden="true"><path d="M6.6 10.8a15 15 0 0 0 6.6 6.6l2.2-2.2a1 1 0 0 1 1-.25 11.4 11.4 0 0 0 3.6.57 1 1 0 0 1 1 1V20a1 1 0 0 1-1 1A17 17 0 0 1 3 4a1 1 0 0 1 1-1h3.5a1 1 0 0 1 1 1c0 1.25.2 2.45.57 3.57a1 1 0 0 1-.25 1z"/></svg>
        0400 555 017
      </li>
      <li>
        <svg viewBox="0 0 24 24" aria-hidden="true"><path d="M2 5h20v14H2zm2 2v.4l8 5 8-5V7z"/></svg>
        info@harlowbuildgroup.com.au
      </li>
      <li>
        <svg viewBox="0 0 24 24" aria-hidden="true"><circle cx="12" cy="12" r="10"/></svg>
        www.harlowbuildgroup.com.au
      </li>
    </ul>
  </section>

</main>
</body>
</html>
```